Printed Promo Flyer for new pet business

We need a double sided flyer design as per the given example flyer, just better looking and more fun.Flyers will need to be printed.Flyer size approx 10.5cm x 15cm. The text will need to be amended slightly afterwards to be more fun unless you can create a new tone of voice as well (should sound fun like breezy do it) Look and Feel: emotional, fun, loving, professional
See attached files.

Target Market(s)

Pet owners in the UK who want the convenience of getting their pets parasite treatment delivered to their door without the need of having to run to the vet or store for purchase

Industry/Entity Type

Pet Care

Colors
00a990
6b449b

Requirements
Must have
• all the content context as given in the example flyer.
Nice to have
• Tone of voice can be changed to be more fun (using Breezy as a guide)

```html
<!DOCTYPE html>
<html lang="en">
<head>
<meta charset="UTF-8">
<title>Pet Parcel – Double-sided Flyer</title>
<link href="https://fonts.googleapis.com/css2?family=Baloo+2:wght@700;800&family=Nunito:wght@600;700;800&display=swap" rel="stylesheet">
<style>
  :root {
    --purple: #6b449b;
    --purple-soft: #efe8f7;
    --teal: #00a990;
    --teal-soft: #e2f5f1;
    --ink: #2a1f3a;
    --paper: #ffffff;
    --table: #e9e4ef;
  }
  * { margin: 0; padding: 0; box-sizing: border-box; }
  html, body { width: 840px; height: 1200px; overflow: hidden; background: var(--table); }
  body { font-family: "Nunito", sans-serif; color: var(--ink); }

  .sheet { position: relative; width: 840px; height: 1200px; }
  .face {
    position: absolute; left: 0; width: 840px; height: 588px;
    background: var(--paper); overflow: hidden; border-radius: 18px;
  }
  .face--front { top: 0; }
  .face--back { top: 612px; }

  /* Front */
  .front-header { position: absolute; left: 0; top: 0; width: 840px; height: 170px; }
  .front-title {
    position: absolute; left: 48px; top: 38px;
    font-family: "Baloo 2", sans-serif; font-weight: 800;
    font-size: 60px; line-height: 1; color: #fff; letter-spacing: 0.5px;
  }
  .benefits {
    position: absolute; left: 48px; top: 190px; width: 744px;
    display: grid; grid-template-columns: 360px 360px; gap: 22px 24px;
  }
  .benefit {
    position: relative; height: 170px; border-radius: 22px; padding: 26px 22px 0 92px;
  }
  .benefit--teal { background: var(--teal-soft); }
  .benefit--purple { background: var(--purple-soft); }
  .benefit__dot {
    position: absolute; left: 24px; top: 26px; width: 50px; height: 50px; border-radius: 50%;
    display: flex; align-items: center; justify-content: center;
  }
  .dot--teal { background: var(--teal); }
  .dot--purple { background: var(--purple); }
  .benefit__title {
    font-family: "Baloo 2", sans-serif; font-weight: 800; font-size: 27px; line-height: 1.1;
  }
  .benefit--teal .benefit__title { color: var(--teal); }
  .benefit--purple .benefit__title { color: var(--purple); }
  .benefit__text { margin-top: 8px; font-size: 17px; font-weight: 700; line-height: 1.4; }

  /* Back */
  .back-title {
    position: absolute; left: 48px; top: 34px;
    font-family: "Baloo 2", sans-serif; font-weight: 800; font-size: 56px; line-height: 1; color: var(--purple);
  }
  .steps { position: absolute; left: 48px; top: 124px; list-style: none; }
  .step { display: flex; align-items: center; height: 50px; margin-bottom: 22px; }
  .step__num {
    flex: none; width: 50px; height: 50px; border-radius: 50%; color: #fff;
    font-family: "Baloo 2", sans-serif; font-weight: 800; font-size: 28px; line-height: 1;
    display: flex; align-items: center; justify-content: center; padding-top: 4px;
  }
  .step__text { margin-left: 20px; font-size: 20px; font-weight: 700; white-space: nowrap; }

  .offer {
    position: absolute; left: 560px; top: 110px; width: 240px; height: 240px; border-radius: 50%;
    background: var(--teal); color: #fff; text-align: center; transform: rotate(-6deg);
  }
  .offer::before {
    content: ""; position: absolute; inset: 10px; border-radius: 50%; border: 3px dashed rgba(255,255,255,0.7);
  }
  .offer__label { position: absolute; top: 58px; width: 100%; font-family: "Baloo 2", sans-serif; font-weight: 700; font-size: 36px; line-height: 1; }
  .offer__price { position: absolute; top: 98px; width: 100%; font-family: "Baloo 2", sans-serif; font-weight: 800; font-size: 62px; line-height: 1; }
  .offer__code { position: absolute; top: 168px; width: 100%; font-size: 17px; font-weight: 800; letter-spacing: 0.5px; }

  .back-footer {
    position: absolute; left: 0; bottom: 0; width: 840px; height: 64px; background: var(--purple);
    display: flex; align-items: center; justify-content: center;
  }
  .site-url { color: #fff; font-size: 22px; font-weight: 800; letter-spacing: 1px; }
</style>
</head>
<body>
<main class="sheet">

  <section class="face face--front" aria-label="Flyer front">
    <svg class="front-header" viewBox="0 0 840 170" aria-hidden="true">
      <path d="M0 0H840V128C700 168 560 112 420 138C280 164 140 112 0 142Z" fill="#6b449b"/>
      <circle cx="700" cy="48" r="44" fill="#00a990" opacity="0.9"/>
      <circle cx="782" cy="104" r="20" fill="#ffffff" opacity="0.25"/>
      <circle cx="628" cy="110" r="12" fill="#ffffff" opacity="0.3"/>
    </svg>
    <h1 class="front-title">Why PET PARCEL?</h1>

    <div class="benefits">
      <article class="benefit benefit--teal">
        <span class="benefit__dot dot--teal"><svg width="24" height="24" viewBox="0 0 24 24"><path d="M5 12.5l4.5 4.5L19 7.5" fill="none" stroke="#fff" stroke-width="3.2" stroke-linecap="round" stroke-linejoin="round"/></svg></span>
        <h2 class="benefit__title">Protection &amp; Care</h2>
        <p class="benefit__text">Full cover against all major parasites, so your pet and family stay safe.</p>
      </article>
      <article class="benefit benefit--purple">
        <span class="benefit__dot dot--purple"><svg width="24" height="24" viewBox="0 0 24 24"><path d="M5 12.5l4.5 4.5L19 7.5" fill="none" stroke="#fff" stroke-width="3.2" stroke-linecap="round" stroke-linejoin="round"/></svg></span>
        <h2 class="benefit__title">In Time</h2>
        <p class="benefit__text">Never remember when to treat your pet again. We do it for you!</p>
      </article>
      <article class="benefit benefit--purple">
        <span class="benefit__dot dot--purple"><svg width="24" height="24" viewBox="0 0 24 24"><path d="M5 12.5l4.5 4.5L19 7.5" fill="none" stroke="#fff" stroke-width="3.2" stroke-linecap="round" stroke-linejoin="round"/></svg></span>
        <h2 class="benefit__title">Convenient</h2>
        <p class="benefit__text">Pops straight through your letter box. No vet or shop runs.</p>
      </article>
      <article class="benefit benefit--teal">
        <span class="benefit__dot dot--teal"><svg width="24" height="24" viewBox="0 0 24 24"><path d="M5 12.5l4.5 4.5L19 7.5" fill="none" stroke="#fff" stroke-width="3.2" stroke-linecap="round" stroke-linejoin="round"/></svg></span>
        <h2 class="benefit__title">Low Cost</h2>
        <p class="benefit__text">All the high-end, trusted brands, but cheaper than the vet.</p>
      </article>
    </div>
  </section>

  <section class="face face--back" aria-label="Flyer back">
    <h1 class="back-title">How it works?</h1>
    <ol class="steps">
      <li class="step"><span class="step__num dot--teal">1</span><span class="step__text">Pick which furry friend it's for</span></li>
      <li class="step"><span class="step__num dot--purple">2</span><span class="step__text">Choose your treatment type</span></li>
      <li class="step"><span class="step__num dot--teal">3</span><span class="step__text">Select your preferred brand</span></li>
      <li class="step"><span class="step__num dot--purple">4</span><span class="step__text">Choose a 1, 3, 6 or 12 month box</span></li>
    </ol>

    <aside class="offer">
      <div class="offer__label">First Box</div>
      <div class="offer__price">£5.99</div>
      <div class="offer__code">Use code : xxx</div>
    </aside>

    <footer class="back-footer"><span class="site-url">www.petparcel.co.uk</span></footer>
  </section>

</main>
</body>
</html>
```